Trifold Brochure needed for Hearthline Counseling

Hi! We need to have a trifold brochure made.

We would like to see brochure designs that use our logo colors, which are khaki, chocolate brown, and gray.

The brochure should be a modern design and please use your creativity.

Brochure is a trifold brochure, size is 8.5 x 11 and full color.

The following attachment has the content to be used in the trifold brochure, as well as some possible pictures. I have also attached our logo.

We would like to use file #2 for sure (picture number 31759204) and add the quote from her...

"At first, I was reluctant about going to Hearthline. Once I got there, I was glad I went. I learned a lot and was treated like family the whole time." Marlene Oakes

Requirements
Must have
• Our logo
• Information should be listed exactly as the attached document
• You must stick with our logo colors

```html
<!DOCTYPE html>
<html lang="en">
<head>
<meta charset="utf-8">
<title>Hearthline Counseling – Trifold Brochure</title>
<link href="https://fonts.googleapis.com/css2?family=Titillium+Web:wght@400;600;700&family=Cinzel:wght@400;700&display=swap" rel="stylesheet">
<style>
  :root {
    --chocolate: #6e4322;
    --chocolate-light: #8a5632;
    --khaki-brown: #7a4a26;
    --gray-text: #5a5a5a;
    --gray-band: #7b7b7b;
    --gray-pill: #6d6d6d;
    --night: #1d1a19;
    --paper-top: #ececec;
    --paper-bottom: #ffffff;
    --white: #ffffff;
  }
  * { box-sizing: border-box; margin: 0; padding: 0; }
  html, body { width: 1200px; height: 927px; overflow: hidden; background: #fff; }
  .brochure {
    position: relative;
    width: 1200px; height: 927px; overflow: hidden;
    background: linear-gradient(180deg, var(--paper-top) 0%, var(--paper-bottom) 70%);
    font-family: "Titillium Web", Arial, sans-serif;
    color: var(--gray-text);
  }
  .rule {
    position: absolute; top: 60px; left: 0; width: 800px; height: 2px;
    background: var(--chocolate);
  }
  .section-bar {
    position: absolute; top: 43px; height: 36px; width: 314px;
    background: var(--chocolate); color: var(--white);
    font-weight: 700; font-size: 19px; letter-spacing: .3px;
    display: flex; align-items: center; justify-content: center;
  }
  .section-bar--faq { left: 43px; }
  .section-bar--reminders { left: 443px; }

  .faq {
    position: absolute; left: 43px; top: 103px; width: 330px;
    font-size: 15px; line-height: 16.5px;
  }
  .faq dt { font-weight: 700; }
  .faq dd { margin-bottom: 17px; }

  .reminders {
    position: absolute; left: 430px; top: 103px; width: 340px;
    text-align: center; font-size: 15px; line-height: 20px;
  }
  .reminders p { margin-bottom: 20px; }
  .reminders strong { font-weight: 700; }

  .motto {
    position: absolute; left: 838px; top: 122px; width: 330px;
    font-family: "Cinzel", Georgia, serif; color: var(--khaki-brown);
    font-size: 25px; line-height: 34px;
  }
  .motto .line1 { display: block; padding-left: 52px; }
  .motto .one { font-size: 46px; font-weight: 700; }
  .motto .line3 { display: block; padding-left: 150px; }

  .art { position: absolute; inset: 0; }

  .contact {
    position: absolute; right: 443px; top: 773px; text-align: right;
  }
  .contact-pill {
    display: inline-block; background: var(--gray-pill); color: var(--white);
    font-size: 15px; padding: 1px 10px; border-radius: 4px 4px 0 0;
  }
  .contact-phone {
    display: block; color: var(--chocolate-light); font-weight: 700;
    font-size: 24px; line-height: 30px; margin-top: 6px;
  }
  .contact-email { display: block; color: #a8a8a8; font-size: 15px; }

  .brand {
    position: absolute; left: 848px; top: 790px; width: 320px;
  }
  .brand-name {
    display: flex; align-items: center; gap: 12px;
    color: #a6a6a6; font-weight: 600; font-size: 38px; line-height: 44px;
  }
  .brand-name::before {
    content: ""; width: 26px; height: 26px; border-radius: 50%;
    background: #a6a6a6; flex: none;
  }
  .brand-tag { color: #d8d8d8; font-size: 16px; margin-top: 14px; letter-spacing: .2px; }
</style>
</head>
<body>
<main class="brochure">
  <svg class="art" width="1200" height="927" viewBox="0 0 1200 927" aria-hidden="false">
    <defs>
      <linearGradient id="couplePhotoRight" x1="0" y1="0" x2="1" y2="1">
        <stop offset="0" stop-color="#dfe6d6"/>
        <stop offset=".5" stop-color="#c9a48a"/>
        <stop offset="1" stop-color="#8a5a45"/>
      </linearGradient>
      <linearGradient id="couplePhotoLeft" x1="0" y1="0" x2="1" y2="1">
        <stop offset="0" stop-color="#cbc3b4"/>
        <stop offset=".5" stop-color="#a08c74"/>
        <stop offset="1" stop-color="#7a4a24"/>
      </linearGradient>
    </defs>
    <rect x="800" y="305" width="400" height="420" fill="url(#couplePhotoRight)" role="img" aria-label="Photo of a smiling senior couple embracing outdoors"/>
    <path d="M0,690 C180,610 420,600 600,688 C680,650 750,630 820,618 L820,927 L0,927 Z" fill="var(--gray-band)"/>
    <path d="M0,708 C180,628 420,618 600,706 C680,668 750,648 820,636 L820,927 L0,927 Z" fill="var(--chocolate)"/>
    <path d="M0,770 C150,700 380,670 555,720 L420,927 L0,927 Z" fill="url(#couplePhotoLeft)" role="img" aria-label="Photo of a happy senior couple lying in autumn leaves"/>
    <path d="M375,927 C440,790 620,705 820,690 C960,680 1100,690 1200,700 L1200,927 Z" fill="var(--night)"/>
  </svg>

  <div class="rule"></div>
  <h2 class="section-bar section-bar--faq">FAQ</h2>
  <h2 class="section-bar section-bar--reminders">APPOINTMENT REMINDERS</h2>

  <dl class="faq">
    <dt>What can I expect at my appointment?</dt>
    <dd>You can Expect to be treated like family throughout the entire visit. We will Respect your time and are dedicated to helping you better understand proactive opioid education.</dd>
    <dt>How long will my appointment last?</dt>
    <dd>Please allow 45 minutes to complete your visit. (this allows time to complete your paperwork)</dd>
    <dt>Will my information be kept confidential?</dt>
    <dd>Yes, your visit will only be shared with your referring doctor. Hearthline Counseling is HIPAA Compliant.</dd>
    <dt>Why do you need my ID and Insurance Card?</dt>
    <dd>Your ID and insurance card are needed for verification and any labs tests that may be requested.</dd>
    <dt>How much is my visit?</dt>
    <dd>The office visit is only $40.<br>( we have a hardship program for those in need)</dd>
    <dt>Is this visit a one time appointment?</dt>
    <dd>Hearthline sees patients 3 to 4 times a year Providing New Educational material and tools each time. (too much information for 1 visit.)</dd>
  </dl>

  <section class="reminders">
    <p><strong>Please bring Picture ID and<br>Insurance Card (s)</strong></p>
    <p><strong>Please allow us up to 45 mins of your time<br>to give you the best possible experience.</strong></p>
    <p><strong>Our office visit is only $40.</strong><br>We accept credit, your check or cash.</p>
    <p><strong>We are anxious to see You!</strong><br>Please do not miss your appointment,<br>a 25.00 no show fee will be applied.</p>
    <p>Hearthline is a stepping stone for Future Success, and Your Future Success should be determined by how much You impact Your community.</p>
    <p><strong>Therefore, let’s work Together in Making Solutions, One Patient at a time.</strong></p>
  </section>

  <p class="motto">
    <span class="line1">"Making Solutions</span>
    <span class="one">ONE</span> Patient
    <span class="line3">at a Time ."</span>
  </p>

  <address class="contact" style="font-style:normal">
    <span class="contact-pill">Contact us at</span>
    <span class="contact-phone">404.555.0182</span>
    <span class="contact-email">info@hearthlinecounseling.com</span>
  </address>

  <div class="brand">
    <div class="brand-name">Hearthline Counseling</div>
    <div class="brand-tag">a pro-active opioid education center</div>
  </div>
</main>
</body>
</html>
```